Northgate Roofing Works Inc Business cards

Commercial and Residential Roofing contractor needs design logo and card design. Can be single or double sided but must incorporate:
Persons Name:
Persons Title:
Mailing Address: PO Box 3719
Physical Address: 58 Fenwick Lane
Halverton, Ma. 01893
800-316-5842
508-712-5842
Fax: 508-712-5867
Cell: Person Cell number
email address
Website: WWW.northgateroofworks.com

Target Market(s)

Residential home owners and commercial building owners

Industry/Entity Type

Roofing

Contact Information for Business Card

Persons Name:
Persons Title:
Halverton, Ma. 01893
800-316-5842
508-712-5842
Fax: 508-712-5867
Cell: Person Cell number
email address

Logo Text

Large enough to service small enough to care

Font styles to use
Serif

Colors
0355a3

Requirements
Must have
• Commercial and Residential Roofing contractor needs design logo and card design. Can be single or double sided but must incorporate:
• Persons Name:
• Persons Title:
• Mailing Address: PO Box 3719
• Physical Address: 58 Fenwick Lane
• Halverton, Ma. 01893
• 800-316-5842
• 508-712-5842
• Fax: 508-712-5867
• Cell: Person Cell number
• email address
• Website: WWW.northgateroofworks.com
Nice to have
• ..
Should not have
• I'm looking for something different. I have had the same card for 23 years. I attached what both sides of my present card looks like.

```html
<!DOCTYPE html>
<html lang="en">
<head>
<meta charset="utf-8">
<title>Northgate Roofing Works Inc – Business Cards</title>
<link href="https://fonts.googleapis.com/css2?family=Open+Sans:wght@400;600;700&display=swap" rel="stylesheet">
<style>
  :root {
    --brand-blue: #0355a3;
    --brand-blue-light: #0b82d2;
    --card-white: #ffffff;
    --card-grey: #e6e8ea;
    --page-bg: #ecebe8;
    --text-white: #ffffff;
  }
  * { box-sizing: border-box; margin: 0; padding: 0; }
  html, body {
    width: 1200px; height: 1023px; overflow: hidden;
    background: var(--page-bg);
    font-family: "Open Sans", sans-serif;
  }
  .stage {
    width: 1200px; height: 1023px;
    display: flex; align-items: center; justify-content: center; gap: 40px;
  }
  .card {
    width: 540px; height: 309px;
    border-radius: 14px; overflow: hidden; position: relative;
    box-shadow: 0 6px 18px rgba(0,0,0,0.18);
  }
  /* Front */
  .card-front {
    background: radial-gradient(ellipse at 62% 40%, var(--brand-blue-light) 0%, var(--brand-blue) 85%);
    color: var(--text-white);
  }
  .front-brand {
    position: absolute; left: 28px; top: 0; bottom: 44px; width: 216px;
    display: flex; align-items: center; gap: 9px;
  }
  .brand-dot {
    width: 12px; height: 12px; flex: none; border-radius: 50%;
    background: var(--text-white);
  }
  .front-brand .brand-name {
    font-size: 19px; font-weight: 700; line-height: 1.2; color: var(--text-white);
    white-space: nowrap;
  }
  .divider {
    position: absolute; left: 250px; top: 46px; height: 174px; width: 1px;
    background: rgba(255,255,255,0.55);
  }
  .person {
    position: absolute; left: 276px; top: 30px;
  }
  .person-name { font-size: 22px; font-weight: 700; letter-spacing: 0.3px; white-space: nowrap; }
  .person-title { font-size: 12px; font-weight: 400; text-align: right; margin-top: -2px; }
  .contact-list {
    position: absolute; left: 276px; top: 98px; list-style: none;
    font-size: 12.5px; line-height: 22px; white-space: nowrap;
  }
  .contact-list li { display: flex; align-items: center; gap: 8px; }
  .contact-list svg { width: 12px; height: 12px; flex: none; fill: none; stroke: var(--text-white); stroke-width: 1.6; }
  .address-strip {
    position: absolute; left: 0; right: 0; bottom: 0; height: 44px;
    background: linear-gradient(var(--card-white), var(--card-grey));
    color: var(--brand-blue);
    font-size: 13px; letter-spacing: 0.3px; white-space: nowrap;
    display: flex; align-items: center; justify-content: center;
  }
  /* Back */
  .card-back {
    background: radial-gradient(ellipse at 45% 40%, var(--card-white) 0%, var(--card-grey) 100%);
    display: flex; align-items: center; justify-content: center;
  }
  .back-brand { display: flex; align-items: center; gap: 14px; }
  .back-brand .brand-dot { width: 20px; height: 20px; background: var(--brand-blue); }
  .back-brand .brand-name {
    font-size: 30px; font-weight: 700; color: var(--brand-blue); line-height: 1.15; white-space: nowrap;
  }
</style>
</head>
<body>
<main class="stage">
  <section class="card card-front" aria-label="Card front">
    <div class="front-brand">
      <span class="brand-dot"></span>
      <span class="brand-name">Northgate Roofing<br>Works Inc.</span>
    </div>
    <div class="divider"></div>
    <div class="person">
      <div class="person-name">Dale Whitcombe</div>
      <div class="person-title">President</div>
    </div>
    <ul class="contact-list">
      <li><svg viewBox="0 0 12 12"><path d="M3 1 L5 3.5 L4 5 Q5.5 7.5 7 8 L8.5 7 L11 9 L9.5 11 Q4 10 1 3 Z"/></svg>800-316-5842</li>
      <li><svg viewBox="0 0 12 12"><rect x="1" y="4" width="10" height="7"/><path d="M3 4 V1 H9 V4"/></svg>508-712-5867</li>
      <li><svg viewBox="0 0 12 12"><rect x="1" y="3" width="10" height="8" rx="1"/><circle cx="6" cy="7" r="2"/></svg>058-441-2093</li>
      <li><svg viewBox="0 0 12 12"><circle cx="6" cy="6" r="5"/><path d="M1 6 H11 M6 1 Q2.5 6 6 11 M6 1 Q9.5 6 6 11"/></svg>www.northgateroofworks.com</li>
      <li><svg viewBox="0 0 12 12"><rect x="3" y="1" width="6" height="10" rx="1"/><path d="M5 9.5 H7"/></svg>508-712-5842</li>
      <li><svg viewBox="0 0 12 12"><rect x="1" y="2.5" width="10" height="7"/><path d="M1 2.5 L6 7 L11 2.5"/></svg>dale@northgateroofworks.com</li>
    </ul>
    <div class="address-strip">58 Fenwick Lane Halverton, Ma. 01893 PO Box 3719</div>
  </section>

  <section class="card card-back" aria-label="Card back">
    <div class="back-brand">
      <span class="brand-dot"></span>
      <span class="brand-name">Northgate Roofing<br>Works Inc.</span>
    </div>
  </section>
</main>
</body>
</html>
```